Design ecommerce website for www.velmorissa.com

Design a Website given below details
Name - www.velmorissa.com

Given a shopify theme :Brightcart
http://layoutbazaar.net/item/brightcart-responsive-shopify-theme/4817203

Given type of products that will be sold
http://tarokbars.pelisite.com
Wendlomart.in
( above designs are not good )

Given competitors
www.zorbelle.com ( especially like how each category is sold as a story )
www.gindova.com

Given Tg
Women 20 +
Aspirational

Website has to be fresh peppy and understated sexy

No need to push Organic agenda too much but it is present in background story

Let me know if any more info required
Updates

Reason: Look for forward to revised designs / new designs

Target Market(s)

Women
20 +
Primarily Indian
Aspirational

Industry/Entity Type

Hair And Beauty

Number of Pages Required

5+ page

Font styles to use
Sans Serif

Requirements
Must have
• Hi Quality Images ( i will provide images )
• Good fun icons
• Good font
• Peppy / classy color scheme
• THe main focus is on the main page / landing page. Need a design which is intuitive and lends itself well to beauty products. Creating an exclusive experiance for women
• The other pages are
• Modified page for product categories ( eg page for all Skin products )
• Modified page for each product
• About page / Check out page
• These are essentially modifications to main page with minor alterations
• Important to remember that we are building using the Brightcart Shopify theme.
• If you recommend shopify apps, I would purchase those too.
Nice to have
• Disctintive fonts.
• Usage of elements/ fonts / icons which make the site very quirky and fun
• I am open to suggestions to changes in words or using images instead of words to convey information
Should not have
• Too much of green / organic feel
• Too much artificial feel ( no neons )

```html
<!DOCTYPE html>
<html lang="en">
<head>
<meta charset="utf-8">
<title>Velmorissa – Natural Beauty Store</title>
<link rel="stylesheet" href="https://fonts.googleapis.com/css2?family=Open+Sans:wght@400;600;700;800&family=Oswald:wght@500;700&family=Dancing+Script:wght@700&display=swap">
<style>
:root{
  --promo:#f3e53c;
  --promo-dark:#1d8fcf;
  --brand:#7cb342;
  --blue:#3c9fd8;
  --blue-dark:#2a86bf;
  --ink:#2b2b2b;
  --muted:#8a8a8a;
  --line:#dcdcdc;
  --soft:#f4f4f4;
  --price:#e0493a;
  --white:#ffffff;
  --footer:#f7f7f7;
}
*{box-sizing:border-box;margin:0;padding:0}
html,body{width:1200px;height:2648px;overflow:hidden;background:var(--white)}
body{font-family:"Open Sans",Arial,sans-serif;color:var(--ink);position:relative}
.wrap{width:1040px;margin:0 auto;position:relative}

/* promo */
.promo{height:80px;background:var(--promo);}
.promo .wrap{display:flex;align-items:center;height:80px;gap:24px}
.promo-photo{width:150px;height:80px;background:linear-gradient(90deg,#e9c8a7,#c79a78)}
.promo-text{flex:1;text-align:center;font-weight:800;font-size:17px;line-height:21px;color:var(--ink);text-transform:uppercase}
.promo-deal{font-family:"Oswald",sans-serif;font-size:38px;color:var(--blue-dark);display:flex;align-items:center;gap:6px}
.promo-deal small{font-size:14px;line-height:16px;display:block}
.promo-btn{background:var(--price);color:var(--white);font-weight:700;font-size:14px;padding:10px 18px;border-radius:3px}

/* header */
.header{height:104px}
.header .wrap{display:flex;align-items:center;height:104px;justify-content:space-between}
.logo{display:flex;align-items:center;gap:12px;font-size:34px;font-weight:700;color:var(--brand)}
.logo-dot{width:22px;height:22px;border-radius:50%;background:var(--brand)}
.header-tools{display:flex;gap:44px}
.tool{display:flex;align-items:center;gap:10px}
.tool svg{width:26px;height:26px}
.tool b{display:block;font-size:12px;text-transform:uppercase}
.tool span{font-size:11px;color:var(--muted)}

/* nav */
.nav{height:30px;background:var(--blue)}
.nav .wrap{display:flex;align-items:center;height:30px;gap:46px}
.nav a{color:var(--white);font-size:12px;font-weight:700;text-decoration:none;text-transform:uppercase}
.nav .search{margin-left:auto;width:200px;height:20px;background:var(--white);font-size:10px;color:var(--muted);padding:3px 8px}

/* hero */
.hero{height:500px;background:linear-gradient(100deg,#ececec 0%,#dcdcdc 45%,#b9b0aa 70%,#8e8079 100%);position:relative}
.hero .wrap{height:500px}
.hero-copy{position:absolute;left:0;top:120px}
.hero-copy h1{font-size:62px;font-weight:700;letter-spacing:-1px;color:var(--ink)}
.hero-copy p{font-size:20px;line-height:28px;width:420px;margin:10px 0 24px}
.btn-outline{display:inline-block;border:2px solid var(--ink);padding:10px 14px;font-weight:700;font-size:18px;text-transform:uppercase}
.dots{position:absolute;right:40px;bottom:22px;display:flex;gap:7px}
.dots i{width:10px;height:10px;border-radius:50%;background:var(--white);opacity:.6}
.dots i:first-child{opacity:1}

/* signup */
.signup{margin-top:16px}
.signup .wrap{height:44px;border-top:1px solid var(--line);border-bottom:1px solid var(--line);display:flex;align-items:center;justify-content:center;gap:30px;background:var(--soft)}
.signup p{font-size:14px;font-weight:700;text-transform:uppercase}
.btn-dark{background:var(--ink);color:var(--white);font-size:12px;font-weight:700;padding:7px 16px;text-transform:uppercase}

/* tiles */
.tiles .wrap{display:flex;gap:20px;margin-top:24px}
.tile{width:245px;height:368px}
.tile-1{background:linear-gradient(160deg,#6a4a2e,#c89a4c)}
.tile-2{background:linear-gradient(160deg,#c9d9b8,#7aa35a)}
.tile-3{background:linear-gradient(160deg,#2d2d34,#a57a6c)}
.tile-4{background:linear-gradient(160deg,#b98a52,#6e4b2c)}

/* game banner */
.game .wrap{margin-top:12px;height:210px;border:1px solid var(--line);display:flex}
.game-photo{width:220px;background:linear-gradient(90deg,#5a3a30,#b88576)}
.game-photo.right{background:linear-gradient(90deg,#a8a6a4,#4a4644)}
.game-copy{flex:1;text-align:center;padding-top:30px}
.game-copy h2{font-family:"Oswald",sans-serif;font-size:30px;font-weight:700;color:var(--blue-dark)}
.game-copy p{font-size:15px;margin:4px 0 8px}
.game-copy h3{font-family:"Dancing Script",cursive;font-size:42px;color:var(--ink)}
.game-copy h3 em{color:var(--price);font-style:normal}
.game-copy .btn-dark{display:inline-block;margin-top:6px}

/* section title */
.section-title{display:flex;align-items:center;justify-content:center;gap:20px;margin-top:34px}
.section-title span{width:110px;height:1px;background:var(--line)}
.section-title h2{font-size:22px;font-weight:700;text-transform:uppercase;letter-spacing:1px}

/* products */
.products .wrap{display:flex;justify-content:space-between;margin-top:40px;position:relative}
.arrow{position:absolute;top:110px;width:30px;height:30px}
.arrow.left{left:-50px}.arrow.right{right:-50px}
.product{width:232px;text-align:center;padding:14px 12px}
.product.active{border:2px solid var(--line)}
.product-photo{height:180px}
.p1{background:linear-gradient(150deg,#d47a8e,#8a2e3d)}
.p2{background:linear-gradient(150deg,#f2e36b,#d9b53a)}
.p3{background:linear-gradient(150deg,#8c1f24,#d3574a)}
.p4{background:linear-gradient(150deg,#f3e38a,#e8bf4c)}
.product h4{font-size:13px;font-weight:600;margin-top:14px;line-height:18px}
.price{color:var(--price);font-size:13px;font-weight:700;margin-top:6px}
.stars{display:flex;justify-content:center;gap:2px;margin-top:6px;font-size:11px;color:var(--muted);align-items:center}
.stars svg{width:12px;height:12px}
.qty{font-size:13px;margin-top:6px}
.cart{display:inline-block;background:var(--blue);color:var(--white);font-size:11px;font-weight:700;padding:6px 14px;margin-top:8px}

/* testimonials */
.testimonials{margin-top:30px;text-align:center}
.testimonials p.quote{width:960px;margin:22px auto 0;font-size:13px;line-height:21px;color:var(--muted)}
.avatar{width:60px;height:60px;border-radius:50%;margin:22px auto 6px;background:linear-gradient(150deg,#d7b39b,#8d6a58)}
.testimonials .name{font-size:12px;color:var(--muted)}

/* footer */
.contact-row .wrap{margin-top:40px;height:56px;border-top:1px solid var(--line);border-bottom:1px solid var(--line);display:flex;align-items:center;gap:40px;font-size:12px}
.contact-row svg{width:22px;height:22px;vertical-align:middle;margin-right:6px}
.news{display:flex;align-items:center;gap:8px}
.news .field{width:180px;height:24px;border:1px solid var(--line)}
.news .btn{background:var(--blue);color:var(--white);font-size:11px;font-weight:700;padding:5px 12px}
.social{margin-left:auto;display:flex;gap:6px;align-items:center}
.social i{width:22px;height:22px;border-radius:50%;border:1px solid var(--muted);display:block}
.links .wrap{display:flex;justify-content:space-between;padding:26px 0 30px}
.links h5{font-size:13px;font-weight:700;margin-bottom:10px}
.links li{list-style:none;font-size:12px;color:var(--muted);line-height:22px}
.trust .wrap{border-top:1px solid var(--line);height:48px;display:flex;align-items:center;gap:60px;font-size:12px;color:var(--muted)}
.trust svg{width:16px;height:16px;vertical-align:middle;margin-right:6px}
.cards{margin-left:auto;display:flex;gap:6px;align-items:center}
.cards i{width:36px;height:22px;background:#d8d8d8;display:block;border-radius:3px}
.legal{position:absolute;left:0;right:0;bottom:0;height:70px;background:var(--footer);text-align:center;padding-top:16px}
.legal nav{font-size:11px;font-weight:700;text-transform:uppercase;display:flex;justify-content:center;gap:18px}
.legal small{display:block;font-size:11px;color:var(--muted);margin-top:8px}
</style>
</head>
<body>

<section class="promo">
  <div class="wrap">
    <div class="promo-photo" role="img" aria-label="Smiling woman with glowing skin"></div>
    <p class="promo-text">Get the celebrity look,<br>lighten your skin with these top products</p>
    <div class="promo-deal">UPTO 80% <small>%<br>DISCOUNT</small></div>
    <span class="promo-btn">CLICK HERE</span>
  </div>
</section>

<header class="header">
  <div class="wrap">
    <div class="logo"><span class="logo-dot"></span>Velmorissa</div>
    <div class="header-tools">
      <div class="tool"><svg viewBox="0 0 24 24" fill="none" stroke="#3c9fd8" stroke-width="2"><circle cx="12" cy="8" r="4"/><path d="M4 21c0-4 4-6 8-6s8 2 8 6"/></svg><div><b>My Account</b><span>Log in &amp; Register</span></div></div>
      <div class="tool"><svg viewBox="0 0 24 24" fill="none" stroke="#3c9fd8" stroke-width="2"><path d="M5 3h4l2 5-3 2a12 12 0 0 0 6 6l2-3 5 2v4a2 2 0 0 1-2 2A17 17 0 0 1 3 5a2 2 0 0 1 2-2z"/></svg><div><b>Contact Us</b><span>We are here for you</span></div></div>
      <div class="tool"><svg viewBox="0 0 24 24" fill="none" stroke="#3c9fd8" stroke-width="2"><path d="M3 4h3l3 11h10l2-8H7"/><circle cx="10" cy="19" r="1.5"/><circle cx="17" cy="19" r="1.5"/></svg><div><b>Shopping Cart</b><span>0 items – Rs.00</span></div></div>
    </div>
  </div>
</header>

<nav class="nav">
  <div class="wrap">
    <a href="#">Skin</a><a href="#">Hair</a><a href="#">Make Up</a><a href="#">Bath and Body</a>
    <span class="search">Enter Your Search</span>
  </div>
</nav>

<section class="hero" role="img" aria-label="Woman in glasses smiling, soft grey studio backdrop">
  <div class="wrap">
    <div class="hero-copy">
      <h1>Ask The Expert</h1>
      <p>Do you have a question about a skin concern or product?</p>
      <span class="btn-outline">Ask Our Expert</span>
    </div>
    <div class="dots"><i></i><i></i><i></i><i></i></div>
  </div>
</section>

<section class="signup">
  <div class="wrap">
    <p>Catch the season's best recommendations, trial packs, offers, and personalized advice</p>
    <span class="btn-dark">Sign Up Now</span>
  </div>
</section>

<section class="tiles">
  <div class="wrap">
    <div class="tile tile-1" role="img" aria-label="Top 10 lists: beauty products on wooden table"></div>
    <div class="tile tile-2" role="img" aria-label="Natural beauty women: woman with flower crown"></div>
    <div class="tile tile-3" role="img" aria-label="Ask the expert: portrait of a woman"></div>
    <div class="tile tile-4" role="img" aria-label="Submit your natural beauty recipe: homemade scrubs"></div>
  </div>
</section>

<section class="game">
  <div class="wrap">
    <div class="game-photo" role="img" aria-label="Woman with glossy dark hair"></div>
    <div class="game-copy">
      <h2>PLAY THE NATURAL BEAUTY GAME</h2>
      <p>Answer three questions and</p>
      <h3>Get a <em>Special Discount Code</em></h3>
      <span class="btn-dark">Start Now</span>
    </div>
    <div class="game-photo right" role="img" aria-label="Long flowing hair"></div>
  </div>
</section>

<div class="section-title"><span></span><h2>Velmorissa Nice</h2><span></span></div>

<section class="products">
  <div class="wrap">
    <svg class="arrow left" viewBox="0 0 24 24" fill="none" stroke="#8a8a8a" stroke-width="2"><path d="M15 4l-8 8 8 8"/></svg>
    <div class="product">
      <div class="product-photo p1" role="img" aria-label="Almond rose soap bars with petals"></div>
      <h4>Almond Rose: The pure Elixir of Youth from Nature</h4>
      <p class="price">Rs. 149</p>
      <div class="stars"><svg viewBox="0 0 24 24" fill="#f2b01e"><path d="M12 2l3 7h7l-6 4 2 8-6-4-6 4 2-8-6-4h7z"/></svg><svg viewBox="0 0 24 24" fill="#f2b01e"><path d="M12 2l3 7h7l-6 4 2 8-6-4-6 4 2-8-6-4h7z"/></svg><svg viewBox="0 0 24 24" fill="#f2b01e"><path d="M12 2l3 7h7l-6 4 2 8-6-4-6 4 2-8-6-4h7z"/></svg><svg viewBox="0 0 24 24" fill="#f2b01e"><path d="M12 2l3 7h7l-6 4 2 8-6-4-6 4 2-8-6-4h7z"/></svg><svg viewBox="0 0 24 24" fill="#ddd"><path d="M12 2l3 7h7l-6 4 2 8-6-4-6 4 2-8-6-4h7z"/></svg>&nbsp;(4/5)</div>
      <p class="qty">100 gms</p>
    </div>
    <div class="product active">
      <div class="product-photo p2" role="img" aria-label="Aloe lavender body wash bottle"></div>
      <h4>Aloe – Lavender Body Wash (200 ml)</h4>
      <p class="price">Rs. 249</p>
      <span class="cart">ADD TO CART</span>
      <p class="qty">200 ml</p>
    </div>
    <div class="product">
      <div class="product-photo p3" role="img" aria-label="Olive rose soap with roses"></div>
      <h4>Olive Rose: For a luxurious and relaxing bath</h4>
      <p class="price">Rs. 199</p>
      <div class="stars"><svg viewBox="0 0 24 24" fill="#f2b01e"><path d="M12 2l3 7h7l-6 4 2 8-6-4-6 4 2-8-6-4h7z"/></svg><svg viewBox="0 0 24 24" fill="#f2b01e"><path d="M12 2l3 7h7l-6 4 2 8-6-4-6 4 2-8-6-4h7z"/></svg><svg viewBox="0 0 24 24" fill="#f2b01e"><path d="M12 2l3 7h7l-6 4 2 8-6-4-6 4 2-8-6-4h7z"/></svg><svg viewBox="0 0 24 24" fill="#f2b01e"><path d="M12 2l3 7h7l-6 4 2 8-6-4-6 4 2-8-6-4h7z"/></svg><svg viewBox="0 0 24 24" fill="#ddd"><path d="M12 2l3 7h7l-6 4 2 8-6-4-6 4 2-8-6-4h7z"/></svg>&nbsp;(4/5)</div>
      <p class="qty">100 gms</p>
    </div>
    <div class="product">
      <div class="product-photo p4" role="img" aria-label="Royal rose radiant cream jar"></div>
      <h4>Royal Rose: Rose Radiant Cream</h4>
      <p class="price">Rs. 349</p>
      <div class="stars"><svg viewBox="0 0 24 24" fill="#f2b01e"><path d="M12 2l3 7h7l-6 4 2 8-6-4-6 4 2-8-6-4h7z"/></svg><svg viewBox="0 0 24 24" fill="#f2b01e"><path d="M12 2l3 7h7l-6 4 2 8-6-4-6 4 2-8-6-4h7z"/></svg><svg viewBox="0 0 24 24" fill="#f2b01e"><path d="M12 2l3 7h7l-6 4 2 8-6-4-6 4 2-8-6-4h7z"/></svg><svg viewBox="0 0 24 24" fill="#f2b01e"><path d="M12 2l3 7h7l-6 4 2 8-6-4-6 4 2-8-6-4h7z"/></svg><svg viewBox="0 0 24 24" fill="#ddd"><path d="M12 2l3 7h7l-6 4 2 8-6-4-6 4 2-8-6-4h7z"/></svg>&nbsp;(4/5)</div>
      <p class="qty">15 gms</p>
    </div>
    <svg class="arrow right" viewBox="0 0 24 24" fill="none" stroke="#8a8a8a" stroke-width="2"><path d="M9 4l8 8-8 8"/></svg>
  </div>
</section>

<section class="testimonials">
  <div class="section-title"><span></span><h2>Testimonials</h2><span></span></div>
  <p class="quote">Lorem ipsum dolor sit amet, consectetur adipiscing elit, sed do eiusmod tempor incididunt ut labore et dolore magna aliqua. Ut enim ad minim veniam, quis nostrud exercitation ullamco laboris nisi ut aliquip ex ea commodo consequat. Duis aute irure dolor in reprehenderit in voluptate velit esse cillum dolore eu fugiat nulla pariatur. Excepteur sint occaecat cupidatat non proident.</p>
  <div class="avatar" role="img" aria-label="Customer portrait"></div>
  <p class="name">Ritika Mehra</p>
</section>

<section class="contact-row">
  <div class="wrap">
    <span><svg viewBox="0 0 24 24" fill="none" stroke="#3c9fd8" stroke-width="2"><path d="M5 3h4l2 5-3 2a12 12 0 0 0 6 6l2-3 5 2v4a2 2 0 0 1-2 2A17 17 0 0 1 3 5a2 2 0 0 1 2-2z"/></svg>Customer care 000-222-1111</span>
    <div class="news"><svg viewBox="0 0 24 24" fill="none" stroke="#3c9fd8" stroke-width="2"><rect x="3" y="5" width="18" height="14"/><path d="M3 5l9 8 9-8"/></svg><span>Subscribe to<br>Our Newsletter</span><span class="field"></span><span class="btn">SIGN UP</span></div>
    <div class="social">Follow Us On <i></i><i></i><i></i><i></i><i></i><i></i></div>
  </div>
</section>

<section class="links">
  <div class="wrap">
    <div><h5>Velmorissa</h5><ul><li>Who We Are?</li><li>Careers</li><li>Authenticity</li><li>Press</li><li>Testimonials</li><li>Beauty Partners</li></ul></div>
    <div><h5>Help</h5><ul><li>Contact Us</li><li>Frequently Asked Questions</li><li>Shipping &amp; Delivery Policy</li><li>Payments</li><li>Cancellations &amp; Returns</li></ul></div>
    <div><h5>Inspire Me</h5><ul><li>Beauty Book</li><li>Virtual Makeover</li><li>Naturally Fit</li><li>Ask The Experts</li></ul></div>
    <div><h5>My Account</h5><ul><li>My Account</li><li>Order History</li><li>Wish List</li><li>Newsletter</li></ul></div>
    <div><h5>Quick Links</h5><ul><li>Skin</li><li>Hair</li><li>Make Up</li><li>Bath and Body</li></ul></div>
  </div>
</section>

<section class="trust">
  <div class="wrap">
    <span><svg viewBox="0 0 24 24" fill="none" stroke="#8a8a8a" stroke-width="2"><rect x="5" y="11" width="14" height="10"/><path d="M8 11V7a4 4 0 0 1 8 0v4"/></svg>Safe and secure transaction</span>
    <span><svg viewBox="0 0 24 24" fill="none" stroke="#8a8a8a" stroke-width="2"><path d="M4 12l5 5L20 6"/></svg>100% Genuine</span>
    <span><svg viewBox="0 0 24 24" fill="none" stroke="#8a8a8a" stroke-width="2"><rect x="2" y="7" width="13" height="10"/><path d="M15 10h4l3 3v4h-7"/></svg>Shipping fee over 500</span>
    <div class="cards">Payment Options <i></i><i></i><i></i><i></i></div>
  </div>
</section>

<footer class="legal">
  <nav><span>Terms and Condition</span><span>Privacy Policy</span><span>Shipping Policy</span><span>Cancellation and Return Policy</span></nav>
  <small>©2015 Velmorissa. All Rights Reserved.</small>
</footer>

</body>
</html>
```